Webbanner-Design für Vermietung von hundefreundlichen Ferienhäusern
Zielgruppe
Ich biete einmal hundefreundliche Ferienhäuser an und suche andererseits neue Gastgeber, die hundefreundliche Ferienhäuser mit mir vermieten. Nordsee
Aufgabenstellung
Das Banner soll auf jeden Fall gelb sein, sonnengelb. Im Text soll stehen, dass ich gewinnbringend vermarkte und Gästen tolle Häuser biete. www.pfotenferien-am-strandweg.de
Das alte Banner habe ich dazu gefügt. Nur so bitte auf keinen Fall mehr. Ich brauche das Banner, um auf www.kelbornwind.de statt des alten, eine neue Werbung zu machen.

```html
<!DOCTYPE html>
<html lang="de">
<head>
<meta charset="utf-8">
<title>Webbanner Pfotenferien am Strandweg – Platzierung Wetterseite</title>
<link rel="stylesheet" href="https://fonts.googleapis.com/css2?family=Open+Sans:wght@300;400;600;700&display=swap">
<style>
  :root {
    --sun-yellow: #e8d700;
    --deep-blue: #1e3592;
    --page-white: #ffffff;
    --page-grey: #d6d6d6;
    --ink: #1f1f1f;
    --accent-line: #1a9be0;
    --projection: rgba(60, 80, 160, 0.2);
    --rule: #8a8a8a;
    --sponsor-pink: #e0197a;
    --sponsor-blue: #1a5fae;
    --photo-sky: #7fa6cf;
    --photo-sea: #44617c;
    --photo-reed: #a88a5a;
  }
  * { box-sizing: border-box; margin: 0; padding: 0; }
  html, body { width: 1030px; height: 1200px; overflow: hidden; }
  body {
    position: relative;
    font-family: "Open Sans", Arial, sans-serif;
    color: var(--ink);
    background: var(--page-white);
  }
  .stage-top { position: absolute; left: 0; top: 0; width: 1030px; height: 514px; background: var(--page-white); }
  .stage-grey { position: absolute; left: 0; top: 514px; width: 1030px; height: 686px; background: var(--page-grey); }
  .projection { position: absolute; left: 0; top: 0; width: 1030px; height: 760px; }
  .banner { position: absolute; display: block; }
  .banner--hero { left: 234px; top: 162px; width: 563px; height: 215px; }
  .banner--small { left: 280px; top: 670px; width: 232px; height: 88px; }

  .section-title {
    position: absolute; left: 0; top: 564px; width: 1030px;
    text-align: center; font-weight: 300; font-size: 30px; color: #111;
  }
  .accent-rule { position: absolute; left: 486px; width: 58px; height: 3px; background: var(--accent-line); }
  .accent-rule--top { top: 631px; }
  .accent-rule--bottom { top: 807px; }

  .sponsor { position: absolute; text-align: center; font-size: 9px; color: #222; }
  .sponsor-tile {
    background: var(--page-white); display: flex; flex-direction: column;
    justify-content: center; align-items: center; margin-bottom: 3px;
  }
  .sponsor--interior { left: 45px; top: 670px; width: 230px; }
  .sponsor--interior .sponsor-tile { height: 81px; }
  .sponsor--interior .sponsor-name { color: var(--sponsor-pink); font-size: 24px; font-weight: 600; line-height: 1.05; }
  .sponsor--banner { left: 280px; top: 761px; width: 232px; }
  .sponsor--switch { left: 530px; top: 670px; width: 207px; }
  .sponsor--switch .sponsor-tile { height: 81px; }
  .sponsor--switch .sponsor-name { color: var(--sponsor-blue); font-size: 22px; font-weight: 700; line-height: 1.1; }
  .sponsor--photo { left: 754px; top: 670px; width: 231px; }
  .sponsor--photo .sponsor-tile { height: 96px; }
  .sponsor--photo .sponsor-name { color: #111; font-size: 26px; font-weight: 400; letter-spacing: 2px; line-height: 1.1; }
  .sponsor--photo .sponsor-sub { color: #111; font-size: 14px; letter-spacing: 1px; }

  .forecast { position: absolute; left: 55px; top: 846px; width: 605px; }
  .forecast-date { font-size: 11px; font-weight: 700; padding-bottom: 8px; border-bottom: 2px solid var(--rule); }
  .forecast-headline { text-align: center; font-size: 16.5px; font-weight: 600; margin: 14px 0 6px; }
  .forecast-body { font-size: 11.4px; line-height: 16.6px; }
  .forecast-body strong { font-weight: 700; }
  .forecast-author { margin-top: 16.6px; }

  .tides { position: absolute; left: 720px; top: 848px; width: 220px; text-align: center; font-size: 11.4px; line-height: 16.6px; }
  .tides-title { font-weight: 700; }
  .tides-gap { height: 16.6px; }
  .tides-source { font-size: 7px; line-height: 10px; }

  .photobox-ad { position: absolute; left: 735px; top: 1044px; width: 189px; height: 156px; background: var(--page-white); padding: 10px 8px 0; }
  .photobox-name { font-size: 18px; font-weight: 400; text-align: center; color: #333; }
  .photobox-sub { font-size: 7px; text-align: center; color: #777; margin-bottom: 10px; }
  .photobox-visual { height: 100px; border-radius: 12px 12px 0 0; background: linear-gradient(#2e7f9c, #1f6680); }
</style>
</head>
<body>
<svg width="0" height="0" style="position:absolute">
  <defs>
    <linearGradient id="photo-tones" x1="0" y1="0" x2="0" y2="1">
      <stop offset="0" stop-color="#9cbbe0"/>
      <stop offset="0.45" stop-color="#6d8fb5"/>
      <stop offset="0.62" stop-color="#44617c"/>
      <stop offset="1" stop-color="#a88a5a"/>
    </linearGradient>
    <symbol id="holiday-banner" viewBox="0 0 679 259">
      <rect width="679" height="259" fill="url(#photo-tones)" role="img" aria-label="Foto: zwei Möpse am Nordseedeich vor Meer und Himmel"/>
      <polygon points="205,0 679,0 679,132 608,175" fill="var(--sun-yellow)"/>
      <polygon points="215,259 679,259 679,132 608,175 520,150 240,215" fill="var(--deep-blue)"/>
      <text x="662" y="30" text-anchor="end" font-family="Open Sans, sans-serif" font-size="19" font-weight="600" fill="var(--deep-blue)">Wir vermarkten ihr Ferienhaus</text>
      <text x="662" y="54" text-anchor="end" font-family="Open Sans, sans-serif" font-size="19" font-weight="600" fill="var(--deep-blue)">gewinnbringend seit 2001!</text>
      <rect x="577" y="72" width="16" height="16" fill="var(--deep-blue)"/>
      <text x="585" y="117" text-anchor="middle" font-family="Open Sans, sans-serif" font-size="15" fill="var(--deep-blue)">Pfotenferien</text>
      <text x="585" y="133" text-anchor="middle" font-family="Open Sans, sans-serif" font-size="15" fill="var(--deep-blue)">am Strandweg</text>
      <polygon points="22,190 50,172 50,190 218,190 218,245 22,245" fill="var(--sun-yellow)"/>
      <text x="120" y="227" text-anchor="middle" font-family="Open Sans, sans-serif" font-size="24" font-weight="700" fill="var(--deep-blue)">Kiek mol in</text>
      <text x="660" y="216" text-anchor="end" font-family="Open Sans, sans-serif" font-size="17" fill="#ffffff">Ferienhaus buchen! Ferienhaus vermieten!</text>
      <text x="660" y="246" text-anchor="end" font-family="Open Sans, sans-serif" font-size="21.5" font-weight="600" fill="#ffffff">www.pfotenferien-am-strandweg.de</text>
    </symbol>
  </defs>
</svg>

<div class="stage-top"></div>
<div class="stage-grey"></div>

<svg class="projection" viewBox="0 0 1030 760" aria-hidden="true">
  <polygon points="234,377 797,377 512,670 280,670" fill="var(--projection)"/>
</svg>

<svg class="banner banner--hero" viewBox="0 0 679 259" role="img" aria-label="Webbanner Pfotenferien am Strandweg">
  <use href="#holiday-banner"/>
</svg>

<h1 class="section-title">Wettervorhersage</h1>
<div class="accent-rule accent-rule--top"></div>

<div class="sponsor sponsor--interior">
  <div class="sponsor-tile"><span class="sponsor-name">Raumglück Atelier</span><span class="sponsor-name" style="font-size:12px">Lena Jessen</span></div>
  Sponsor
</div>
<svg class="banner banner--small" viewBox="0 0 679 259" role="img" aria-label="Webbanner Pfotenferien am Strandweg, verkleinert">
  <use href="#holiday-banner"/>
</svg>
<div class="sponsor sponsor--banner">Sponsor</div>
<div class="sponsor sponsor--switch">
  <div class="sponsor-tile"><span class="sponsor-name">JORN BREKEL</span><span class="sponsor-name">Schaltanlagen</span></div>
  Sponsor
</div>
<div class="sponsor sponsor--photo">
  <div class="sponsor-tile"><span class="sponsor-name">FOTOGRAFIE</span><span class="sponsor-sub">ARNE LÜTT</span></div>
  Sponsor
</div>
<div class="accent-rule accent-rule--bottom"></div>

<article class="forecast">
  <h2 class="forecast-date">PROGNOSE FÜR DONNERSTAG, DEN 06.12.18</h2>
  <h3 class="forecast-headline">Wind und Wasser</h3>
  <div class="forecast-body">
    <strong>Heute:</strong><br>
    Nach vielen doch insgesamt eher ruhigen Tagen geht es nun etwas turbulenter zu beim Wetter. Schuld daran ist Tief Marielou, welches uns mit seinem Wetter beeinflusst.<br>
    Am Morgen ist es teils noch trocken oder es regnet nur leicht, aber bereits im Laufe des Vormittags zieht von Westen her ein kräftiges Regengebiet auf, das über den Mittag teils starken Regen bringt. Danach wird es zwar - den Norden ausgenommen - kurz nochmal trocken, aber schnell zieht die Kaltfront mit weiteren kräftigen Schauern auf, die uns in und durch die Nacht - von zeitweisen trockenen Phasen, die aber erst am späten Abend dabei sein werden - begleiten werden.<br>
    Der Wind weht zunächst nur mäßig bis frisch aus Süd bis Südwest, frischt aber immer mehr auf, gerade bei und nach Durchzug des ersten Regengebietes. Ab dem Mittag sind dann auch an der Küste Sturm- und in den anderen Landesteilen stürmische Böen dabei. Mit Durchzug der regenreichen Kaltfront sind dann auch im Landesinneren einzelne Sturmböen möglich, ebenso nahe der folgenden Schauer, gerade am späteren Abend. Direkt an der Nordsee sind dann auch örtlich schwere Sturmböen möglich. Dazu dreht der Wind dann auf West.<br>
    Die Temperaturen steigen an auf 9 bis 10 Grad.
    <p class="forecast-author">Jan Holmsen</p>
  </div>
</article>

<aside class="tides">
  <div class="tides-title">Gezeiten Husum</div>
  <div>Fr , 07.12.2018 | H | 1:32 - 6.8</div>
  <div>Fr , 07.12.2018 | N | 7:56 - 3.2</div>
  <div>Fr , 07.12.2018 | H | 13:53 - 6.8</div>
  <div>Fr , 07.12.2018 | N | 20:16 - 3.1</div>
  <div class="tides-gap"></div>
  <div>Sa , 08.12.2018 | H | 2:12 - 6.8</div>
  <div>Sa , 08.12.2018 | N | 8:43 - 3.1</div>
  <div>Sa , 08.12.2018 | H | 14:33 - 6.8</div>
  <div>Sa , 08.12.2018 | N | 20:50 - 3.1</div>
  <div class="tides-source">Quelle: Amt für Küstenpegel und Tiden</div>
</aside>

<div class="photobox-ad">
  <div class="photobox-name">Klick-Kiste-Service</div>
  <div class="photobox-sub">Die Fotobox von Ole Brandt - Fotografie</div>
  <div class="photobox-visual" role="img" aria-label="Illustration einer Kamera in Petrol"></div>
</div>
</body>
</html>
```